Young, modern, highly skilled carpenter needs business card design

I need a business card design for my construction business. Its called 'Pemberton Building Partners'. Im looking for a ultra modern design that incorporates P B P, the first letters of the name with only a subtle reference to carpentry. The design should reflect my high quality work and eye for detail. i have also uploaded some exmaple designs i like.

Industry/Entity Type

Construction

Requirements
Must have
• Name of business, my name, mobile number, ABN number, email address
Nice to have
• A logo incorporating the name of the business

```html
<!DOCTYPE html>
<html lang="en">
<head>
<meta charset="utf-8">
<title>Pemberton Building Partners — Business Card</title>
<link href="https://fonts.googleapis.com/css2?family=Carlito:wght@400;700&display=swap" rel="stylesheet">
<style>
  :root {
    --backdrop: #e6ebeb;
    --kraft: #c9b264;
    --kraft-light: #d2bc70;
    --kraft-dark: #bea554;
    --ink: #111111;
  }
  html, body {
    margin: 0;
    padding: 0;
    width: 1200px;
    height: 900px;
    overflow: hidden;
    background: var(--backdrop);
    font-family: "Carlito", "Calibri", sans-serif;
    color: var(--ink);
  }
  .canvas {
    position: relative;
    width: 1200px;
    height: 900px;
  }
  .card {
    position: absolute;
    left: 334px;
    width: 542px;
    height: 371px;
    background: radial-gradient(ellipse at 40% 35%, var(--kraft-light) 0%, var(--kraft) 55%, var(--kraft-dark) 100%);
  }
  .card--front { top: 62px; }
  .card--back { top: 460px; }

  .front-wordmark {
    position: absolute;
    left: 64px;
    top: 256px;
    margin: 0;
    font-size: 66px;
    font-weight: 700;
    line-height: 1;
    letter-spacing: 2px;
  }

  .back-wordmark {
    position: absolute;
    left: 64px;
    top: 66px;
    margin: 0;
    font-size: 25px;
    font-weight: 400;
    letter-spacing: 1.5px;
    text-transform: uppercase;
    line-height: 1;
  }

  .contact {
    position: absolute;
    left: 66px;
    top: 217px;
    margin: 0;
    font-size: 20px;
    line-height: 26.5px;
    font-style: normal;
  }
  .contact span { display: block; }
</style>
</head>
<body>
  <main class="canvas">
    <section class="card card--front" aria-label="Business card front">
      <p class="front-wordmark">PBP</p>
    </section>

    <section class="card card--back" aria-label="Business card back">
      <p class="back-wordmark">Pemberton Building Partners</p>
      <address class="contact">
        <span class="contact__name">Liam Pemberton</span>
        <span class="contact__email">M: liam_pemberton@mailbox.com</span>
        <span class="contact__phone">T: 0418362051</span>
        <span class="contact__abn">ABN: 51 284 630 917</span>
      </address>
    </section>
  </main>
</body>
</html>
```